New Webpage for High Class Expert Witness Services Company

We are looking for a minimalist design for a webpage that just has our logo and an entry form offer to connect with one of our Liaisons.
The entry form should just ask for Name, Email, Contact Info and Description of Project.

Company Name is: The Marlow Crest Advisory Services

Number of Pages Required

1 page

```html
<!DOCTYPE html>
<html lang="en">
<head>
<meta charset="utf-8">
<title>Connect with a Liaison — The Marlow Crest Advisory Services</title>
<link href="https://fonts.googleapis.com/css2?family=Poppins:wght@400;500;600&display=swap" rel="stylesheet">
<style>
  :root {
    --page-bg: #111726;
    --panel-deep: #0a0f1b;
    --panel-light: #1a202c;
    --line: #c9ccd2;
    --bracket: #e8e9ec;
    --title: #d4d5d8;
    --label: #a3a7ae;
    --text: #ffffff;
    --brand: #c7c9cd;
  }
  * { box-sizing: border-box; margin: 0; padding: 0; }
  html, body {
    width: 1200px; height: 853px; overflow: hidden;
    background: var(--page-bg);
    font-family: "Poppins", sans-serif;
  }
  .page { position: relative; width: 1200px; height: 853px; }

  .brand {
    position: absolute; top: 70px; left: 0; width: 1200px;
    display: flex; justify-content: center; align-items: center; gap: 10px;
  }
  .brand-mark { width: 14px; height: 14px; background: var(--brand); border-radius: 50%; }
  .brand-name {
    font-size: 17px; font-weight: 500; letter-spacing: 2px;
    text-transform: uppercase; color: var(--brand);
  }

  .panel {
    position: absolute; left: 165px; top: 174px; width: 871px; height: 611px;
    border: 1px solid var(--line);
    background: radial-gradient(ellipse at 10% 0%, var(--panel-deep) 0%, var(--page-bg) 55%, var(--panel-light) 100%);
  }
  .corner { position: absolute; width: 35px; height: 35px; border: 0 solid var(--bracket); }
  .corner.tl { left: -4px; top: -4px; border-left-width: 4px; border-top-width: 4px; }
  .corner.tr { right: -4px; top: -4px; border-right-width: 4px; border-top-width: 4px; }
  .corner.bl { left: -4px; bottom: -4px; border-left-width: 4px; border-bottom-width: 4px; }
  .corner.br { right: -4px; bottom: -4px; border-right-width: 4px; border-bottom-width: 4px; }

  .form-title {
    position: absolute; top: 44px; left: 0; width: 100%;
    text-align: center; font-size: 29px; font-weight: 600; color: var(--title);
  }
  .field-label {
    position: absolute; font-size: 11.5px; color: var(--label);
  }
  .field {
    position: absolute; border: 1px solid var(--line); border-radius: 6px;
    color: var(--text); font-size: 12px; padding: 0 11px;
    display: flex; align-items: center;
  }
  .field.area { align-items: flex-start; padding-top: 12px; }
  .country-code { justify-content: space-between; padding: 0 8px; }
  .submit {
    position: absolute; left: 81px; top: 519px; width: 708px; height: 50px;
    border: 1px solid var(--line); border-radius: 6px;
    display: flex; justify-content: center; align-items: center;
    font-size: 20px; font-weight: 500; color: var(--text);
  }
</style>
</head>
<body>
<div class="page">
  <header class="brand">
    <span class="brand-mark"></span>
    <span class="brand-name">The Marlow Crest Advisory Services</span>
  </header>

  <section class="panel">
    <span class="corner tl"></span><span class="corner tr"></span>
    <span class="corner bl"></span><span class="corner br"></span>

    <h1 class="form-title">Connect with a Liaison</h1>

    <span class="field-label" style="left:81px;top:126px">Full NAME*</span>
    <div class="field" style="left:81px;top:148px;width:342px;height:40px">Owen Carter</div>

    <span class="field-label" style="left:447px;top:126px">E-MAIL ADDRESS*</span>
    <div class="field" style="left:447px;top:148px;width:342px;height:40px">owen.carter@mailbox.com</div>

    <span class="field-label" style="left:81px;top:216px">Phone Number</span>
    <div class="field country-code" style="left:81px;top:238px;width:55px;height:40px">
      +91
      <svg width="10" height="6" viewBox="0 0 10 6"><path d="M1 1l4 4 4-4" fill="none" stroke="#fff" stroke-width="1.3"/></svg>
    </div>
    <div class="field" style="left:139px;top:238px;width:650px;height:40px">55512340987</div>

    <span class="field-label" style="left:81px;top:306px">Description of project</span>
    <div class="field area" style="left:81px;top:328px;width:708px;height:155px">Write Description of the project here ....</div>

    <div class="submit">Submit</div>
  </section>
</div>
</body>
</html>
```